Tolvane Handyman Service

File 2 Prep kitchen cabinets
File 3 Painting kitchen cabinets
File 4 Demo stairs
File 5 Completion Installing stair treads
File 6 Power washing deck
File 7 Completion of Sainting deck and railings
File 8 Completion of staining steps
Logo, owner name, email and web site on front cover
File 9 Demo living room floor
File 10 Completion of living room floor
Please see additional on attached flyer

Target Market(s)

Residential

Industry/Entity Type

Painting

Font styles to use
Serif
Sans Serif

Requirements
Must have
• Some Photos and type of work discerption
Front page Logo, web address, phone number, owners name and email address
Back Page see attached file 1
Nice to have
• Photo maybe in middle of flyer
Use the best text that you think will meet the needs
Should not have
• No pink colors

```html
<!DOCTYPE html>
<html lang="en">
<head>
<meta charset="utf-8">
<title>Tolvane Handyman Services – Trifold Brochure</title>
<link href="https://fonts.googleapis.com/css2?family=Oswald:wght@500;600&family=Libre+Baskerville:ital,wght@0,700;1,400&family=Open+Sans:wght@400;600;700&display=swap" rel="stylesheet">
<style>
  :root{
    --navy:#2b3a8f;
    --navy-deep:#233080;
    --blue:#3f5fe6;
    --white:#ffffff;
    --paper:#f7f8fb;
    --ink:#2a2f45;
    --stage:#d6d7da;
  }
  *{box-sizing:border-box;margin:0;padding:0}
  html,body{width:1200px;height:4408px;overflow:hidden}
  body{background:var(--stage);font-family:"Open Sans",Arial,sans-serif;color:var(--ink);position:relative}
  .spread{position:absolute;left:40px;width:1120px;height:794px;display:flex;background:var(--white);box-shadow:0 4px 18px rgba(0,0,0,.18)}
  .spread--outside{top:1320px}
  .spread--inside{top:2260px}
  .panel{position:relative;width:373.33px;height:100%;overflow:hidden}

  /* ---------- back panel / contact ---------- */
  .contact{background:linear-gradient(180deg,var(--navy) 0%,var(--navy-deep) 100%);color:var(--white);text-align:center}
  .contact__title{margin-top:36px;font-family:"Open Sans",sans-serif;font-weight:600;font-size:22px;letter-spacing:5px}
  .contact__box{margin:18px auto 0;width:232px;border:1.5px solid rgba(255,255,255,.55);border-radius:10px;padding:14px 8px 12px;font-size:14px;line-height:21px}
  .contact__icons{display:flex;justify-content:center;gap:6px;margin-top:-26px;margin-bottom:8px;background:var(--navy);width:72px;margin-left:auto;margin-right:auto}
  .contact__icons svg{width:18px;height:18px}
  .contact__box b{font-weight:700}
  .slogan{margin-top:30px;font-family:"Oswald",sans-serif;font-weight:500;font-size:40px;letter-spacing:.5px;line-height:1}
  .promise{margin:36px auto 0;width:318px;height:180px;background:var(--white);border:3px solid var(--blue);outline:2px solid var(--white);display:flex;flex-direction:column;justify-content:center;font-family:"Oswald",sans-serif;font-weight:600;font-size:32px;line-height:42px;color:var(--blue)}
  .perks{list-style:none;margin-top:50px;font-size:16px;line-height:25.5px}
  .perks li{display:block;width:max-content;margin:0 auto;border-bottom:1px solid rgba(255,255,255,.5)}

  /* ---------- inside flap of cover ---------- */
  .flap{background:var(--white)}
  .flap__address{position:absolute;left:24px;bottom:112px;transform-origin:left bottom;transform:rotate(-90deg) translateY(100%);font-size:13.5px;line-height:17px;color:#33384f;width:max-content}
  .flap__brand{position:absolute;left:22px;bottom:36px;display:flex;align-items:center;gap:6px}
  .flap__brand .mark{width:18px;height:18px;border:2px solid var(--blue)}
  .flap__brand span{font-family:"Libre Baskerville",serif;font-weight:700;font-size:8px;color:var(--navy);width:70px;line-height:10px}
  .flap__band{position:absolute;right:0;bottom:0;width:373px;height:60px}

  /* ---------- front cover ---------- */
  .cover{background:var(--white)}
  .brand{position:absolute;top:28px;left:0;right:0;text-align:center}
  .brand .mark{width:54px;height:54px;border:4px solid var(--blue);margin:0 auto 12px}
  .brand__name{font-family:"Libre Baskerville",serif;font-weight:700;font-size:13px;color:var(--navy);line-height:18px}
  .cover__photo{position:absolute;top:190px;left:0;width:100%;height:330px;background:linear-gradient(180deg,#c9ccd0 0%,#b9b5ad 35%,#b47a3e 60%,#8c8d88 85%,#6d8a4a 100%)}
  .cover__chevron{position:absolute;top:170px;left:0;width:100%;height:120px}
  .cover__band{position:absolute;left:0;bottom:0;width:100%;height:300px}
  .cover__text{position:absolute;left:0;right:0;bottom:0;height:285px;text-align:center;color:var(--white)}
  .headline{margin-top:30px;font-family:"Oswald",sans-serif;font-weight:500;font-size:34px;line-height:48px}
  .tagline{margin-top:30px;font-family:"Libre Baskerville",serif;font-style:italic;font-size:16.5px;line-height:22px}
  .web{margin:22px auto 0;width:300px;border:1.5px solid rgba(255,255,255,.7);font-size:13px;letter-spacing:3px;padding:4px 0}

  /* ---------- services ---------- */
  .services{background:var(--white);padding:28px 22px 0 30px}
  .service{height:152px}
  .service__label{display:block;width:176px;margin:0 auto 10px;background:var(--blue);color:var(--white);text-align:center;font-size:14px;font-weight:600;letter-spacing:.5px;padding:2px 0}
  .service__cols{display:flex;gap:14px}
  .service__cols ul{list-style:none;flex:1;font-size:10.5px;line-height:14px}
  .service__cols ul+ul{border-left:1px solid #cfd3e0;padding-left:12px}
  .service__cols li{position:relative;padding-left:15px;margin-bottom:5px}
  .service__cols li::before{content:"";position:absolute;left:0;top:2px;width:10px;height:10px;border-radius:50%;background:var(--navy)}
  .service__cols li::after{content:"";position:absolute;left:3px;top:4px;width:3px;height:5px;border:solid var(--white);border-width:0 1.5px 1.5px 0;transform:rotate(45deg)}

  /* ---------- gallery ---------- */
  .gallery{background:linear-gradient(180deg,var(--navy) 0%,var(--navy-deep) 100%);padding:34px 0 0}
  .gallery__item{width:282px;height:120px;margin:0 auto 34px;border:3px solid var(--white);outline:1px solid rgba(255,255,255,.4)}
  .g1{background:linear-gradient(135deg,#6b4a32,#d8c8b0 60%,#f1ece4)}
  .g2{background:linear-gradient(135deg,#e9e6e1,#bfb8ad 55%,#7a6a55)}
  .g3{background:linear-gradient(160deg,#d9d3c8,#9c8f7b 55%,#5b4e3d)}
  .g4{background:linear-gradient(180deg,#f0ede8,#cbc2b3 50%,#6a5a46)}
  .g5{background:linear-gradient(180deg,#e4e1dc,#4c5058 55%,#8f8a82)}

  /* ---------- mission ---------- */
  .mission{background:var(--white)}
  .mission__title{position:absolute;top:52px;left:30px;font-size:15px;font-weight:700;color:var(--blue)}
  .mission__text{position:absolute;top:78px;left:30px;right:26px;font-size:11px;line-height:14.5px;color:#3b4055;text-align:justify}
  .mission__photo{position:absolute;top:292px;left:34px;width:305px;height:166px;background:linear-gradient(180deg,#5c6a82 0%,#e9ecef 40%,#cfd5da 70%,#7a3a2c 100%)}
  .mission__scene{position:absolute;left:0;bottom:0;width:100%;height:214px;background:linear-gradient(180deg,#c7d3df 0%,#e8ecf0 30%,#b9894c 55%,#8a8f94 72%,#5f9a3c 100%)}
</style>
</head>
<body>

<section class="spread spread--outside">
  <article class="panel contact">
    <h2 class="contact__title">CONTACT</h2>
    <div class="contact__box">
      <div class="contact__icons">
        <svg viewBox="0 0 24 24" aria-hidden="true"><path fill="#fff" d="M6.6 10.8c1.4 2.8 3.8 5.1 6.6 6.6l2.2-2.2c.3-.3.7-.4 1-.2 1.1.4 2.3.6 3.6.6.6 0 1 .4 1 1V20c0 .6-.4 1-1 1C10.6 21 3 13.4 3 4c0-.6.4-1 1-1h3.5c.6 0 1 .4 1 1 0 1.3.2 2.5.6 3.6.1.3 0 .7-.2 1z"/></svg>
        <svg viewBox="0 0 24 24" aria-hidden="true"><path fill="#fff" d="M3 5h18v14H3z"/><path fill="none" stroke="#2b3a8f" stroke-width="2" d="M3 6l9 7 9-7"/></svg>
        <svg viewBox="0 0 24 24" aria-hidden="true"><circle cx="12" cy="12" r="9" fill="none" stroke="#fff" stroke-width="2"/><path fill="none" stroke="#fff" stroke-width="1.6" d="M3 12h18M12 3c3 3 3 15 0 18M12 3c-3 3-3 15 0 18"/></svg>
      </div>
      <p>Owner <b>DALE MARROW</b></p>
      <p>(555) 014-2290</p>
      <p>dale@tolvanehandyman.com</p>
      <p>www.tolvanehandyman.com</p>
    </div>
    <p class="slogan">ONE CALL DOES IT ALL</p>
    <div class="promise">
      <span>FIX IT.</span><span>REPAIR IT.</span><span>CHANGE IT.</span><span>BUILD IT.</span>
    </div>
    <ul class="perks">
      <li>35 years Experience</li>
      <li>Free Written Estimates</li>
      <li>Fully Insured</li>
      <li>Locally Owned</li>
      <li>Prompt Response</li>
      <li>Trained Personnel</li>
      <li>Quality Materials</li>
      <li>References on Request</li>
    </ul>
  </article>

  <article class="panel flap">
    <p class="flap__address">Tolvane Handyman Services<br>18 Birchwood Ln<br>Kestrel, Maine 04000</p>
    <div class="flap__brand"><div class="mark"></div><span>Tolvane Handyman Services</span></div>
    <svg class="flap__band" viewBox="0 0 373 60" preserveAspectRatio="none" aria-hidden="true"><polygon points="190,30 373,18 373,60 170,60" fill="#2b3a8f"/></svg>
  </article>

  <article class="panel cover">
    <div class="brand">
      <div class="mark"></div>
      <p class="brand__name">Tolvane Handyman Services</p>
    </div>
    <div class="cover__photo" role="img" aria-label="Photo of a newly built and stained wooden deck with railings on a grey house"></div>
    <svg class="cover__chevron" viewBox="0 0 373 120" preserveAspectRatio="none" aria-hidden="true">
      <polygon points="0,0 373,0 373,112 186,40 0,112" fill="#fff"/>
      <polyline points="0,80 186,8 373,80" fill="none" stroke="#3f5fe6" stroke-width="9"/>
      <polyline points="0,96 186,24 373,96" fill="none" stroke="#3f5fe6" stroke-width="6"/>
      <polyline points="0,112 186,40 373,112" fill="none" stroke="#3f5fe6" stroke-width="9"/>
    </svg>
    <svg class="cover__band" viewBox="0 0 373 300" preserveAspectRatio="none" aria-hidden="true"><polygon points="0,18 373,0 373,300 0,300" fill="#2b3a8f"/></svg>
    <div class="cover__text">
      <h1 class="headline">WE ARE THE SOLUTION<br>TO YOUR PROBLEMS!</h1>
      <p class="tagline">Serving Southern Maine<br>For All Your Painting<br>And Remodeling Needs</p>
      <p class="web">www.tolvanehandyman.com</p>
    </div>
  </article>
</section>

<section class="spread spread--inside">
  <article class="panel services">
    <div class="service">
      <span class="service__label">INTERIOR PAINTING</span>
      <div class="service__cols">
        <ul><li>Commercial &amp; Residential</li><li>Kitchen Cabinets</li><li>Painting</li></ul>
        <ul><li>Walls trim &amp; doors</li><li>Ceiling repair</li><li>Staining &amp; polying trim</li></ul>
      </div>
    </div>
    <div class="service">
      <span class="service__label">EXTERIOR PAINTING</span>
      <div class="service__cols">
        <ul><li>Commercial &amp; Residential</li><li>New Painting &amp; Updates</li><li>All types of Siding</li><li>Power washing</li></ul>
        <ul><li>Painting &amp; Staining of decks</li><li>Fence cleaning painting &amp; sealing</li><li>Furniture cleaning, painting &amp; sealing</li></ul>
      </div>
    </div>
    <div class="service">
      <span class="service__label">EXTERIOR PAINTING</span>
      <div class="service__cols">
        <ul><li>Commercial &amp; Residential</li><li>Kitchen Cabinets</li><li>Painting</li></ul>
        <ul><li>Walls Trim &amp; Doors</li><li>Ceiling Repair</li><li>Staining &amp; Polying Trim</li></ul>
      </div>
    </div>
    <div class="service">
      <span class="service__label">CARPENTRY</span>
      <div class="service__cols">
        <ul><li>Commercial &amp; Residential</li><li>Kitchen remodeling</li><li>Marble &amp; Granite countertops</li><li>Bathroom remodeling</li><li>Basement remodeling</li></ul>
        <ul><li>Disabled accessible ramps &amp; bathroom ins installation</li><li>Room additions</li><li>All types of siding</li><li>Cabinetry</li><li>Sheet rocking</li></ul>
      </div>
    </div>
    <div class="service">
      <span class="service__label">MAINTENANCE</span>
      <div class="service__cols">
        <ul><li>Commercial &amp; Residential</li><li>Hanging Curtin's &amp; Blinds</li><li>Shelving</li><li>Lighting</li></ul>
        <ul><li>Picture hanging</li><li>TV mounting</li><li>Desk &amp; furniture assembly</li><li>Fixture installation &amp; repair</li></ul>
      </div>
    </div>
  </article>

  <article class="panel gallery">
    <div class="gallery__item g1" role="img" aria-label="Photo of kitchen cabinets being prepped with a ladder"></div>
    <div class="gallery__item g2" role="img" aria-label="Photo of a living room during floor demolition"></div>
    <div class="gallery__item g3" role="img" aria-label="Photo of a completed living room floor"></div>
    <div class="gallery__item g4" role="img" aria-label="Photo of kitchen cabinets after painting"></div>
    <div class="gallery__item g5" role="img" aria-label="Photo of a finished kitchen with dark painted cabinets"></div>
  </article>

  <article class="panel mission">
    <h3 class="mission__title">THE MISSION</h3>
    <p class="mission__text">At Tolvane Handyman Services we are committed to client satisfaction and understanding that customer service is the foundation of our business. We are dedicated to providing our clients with quality workmanship performed in a prompt, professional manner. Our reliable team, second to non, will arrive neat in appearance &amp; ready to work. Our technicians will treat each job, large or small, with the same care we would if we were repairing our own home.</p>
    <div class="mission__photo" role="img" aria-label="Photo of a new window and stained steps on grey siding"></div>
    <div class="mission__scene" role="img" aria-label="Photo of a single-storey house with a fresh lawn"></div>
  </article>
</section>

</body>
</html>
```